Laboratory and geotechnical service provider needs Word template

We require a new Word Template for our business. We are looking for a modern, business-like format. We typically generate reports such as management plans, business plans, method statements, technical reports. These reports cover generally between 5 and 30 pages, but sometimes up to 500 pages including the appendices.

Lab reports have their own formats and are not parts of this scope.

Target Market(s)

We report to Clients such as construction industry contractors, governmental departments and engineering consultants.

Industry/Entity Type

Technical Service

Colors

Designer to choose colors to be used in the design.

Requirements
Must have
• The report needs a fancy cover page with a title field, subtitle, project field, client name field, reference number field. Photo/graphics as background on cover. Second page needs a revision table for document control. Table of contents up to 2 levels. Appendices to be part of TOC. Report first page with custom headings for body text, titles, subtitles, headings 1, 2, 3, etc. Include a table with caption, figure with caption, bullet list, numbered list. Appendix page. Please use fonts consistently, choose a common, but professional, modern font.
Nice to have
• We traditionally use black and yellow as company colours. Please visit our company page www.tarnvalecores.com.
Should not have
• The two attached word documents is what we use now for your information, we are looking for something better!

```html
<!DOCTYPE html>
<html lang="en">
<head>
<meta charset="utf-8">
<title>Report Cover – Tarnvale Cores</title>
<link rel="stylesheet" href="https://fonts.googleapis.com/css2?family=Noto+Serif:wght@400;700&display=swap">
<style>
  :root {
    --brand-yellow: #f2de00;
    --brand-yellow-deep: #e0ca00;
    --ink: #333333;
    --ink-soft: #4a4500;
    --paper: #ffffff;
    --pattern-grey: #cfcfcf;
  }
  html, body {
    margin: 0;
    padding: 0;
    width: 845px;
    height: 1200px;
    overflow: hidden;
    background: var(--paper);
  }
  .cover {
    position: relative;
    width: 845px;
    height: 1200px;
    overflow: hidden;
    background: var(--paper);
    font-family: "Noto Serif", Georgia, serif;
    color: var(--ink);
  }
  .cover__art-top {
    position: absolute;
    top: 0;
    right: 0;
    width: 430px;
    height: 700px;
    background: radial-gradient(ellipse 100% 95% at 100% 0%, var(--pattern-grey) 0%, rgba(207,207,207,0.6) 45%, rgba(255,255,255,0) 80%);
  }
  .cover__band {
    position: absolute;
    left: 0;
    right: 0;
    top: 781px;
    bottom: 0;
    background: var(--brand-yellow);
  }
  .cover__band-notch {
    position: absolute;
    left: 141px;
    top: -25px;
    width: 50px;
    height: 25px;
  }
  .cover__art-bottom {
    position: absolute;
    right: 0;
    top: 20px;
    bottom: 0;
    width: 270px;
    background: radial-gradient(ellipse 120% 90% at 100% 60%, var(--brand-yellow-deep) 0%, rgba(224,202,0,0.7) 50%, rgba(224,202,0,0) 85%);
  }
  .brand {
    position: absolute;
    left: 70px;
    top: 390px;
    height: 160px;
    display: flex;
    align-items: center;
    gap: 16px;
  }
  .brand__square {
    width: 40px;
    height: 40px;
    background: var(--brand-yellow);
  }
  .brand__name {
    font-size: 34px;
    font-weight: 700;
    color: var(--ink);
  }
  .report-title {
    position: absolute;
    left: 70px;
    top: 580px;
    margin: 0;
    font-size: 42px;
    line-height: 1.2;
    font-weight: 700;
  }
  .report-subtitle {
    position: absolute;
    left: 70px;
    top: 654px;
    margin: 0;
    font-size: 34px;
    line-height: 1.2;
    font-weight: 700;
  }
  .report-fields {
    position: absolute;
    left: 70px;
    top: 90px;
    margin: 0;
    display: grid;
    grid-template-columns: 190px 260px;
    row-gap: 22px;
    font-size: 21px;
    line-height: 1.3;
  }
  .report-fields dt {
    font-weight: 700;
    color: var(--ink);
  }
  .report-fields dd {
    margin: 0;
    font-weight: 400;
    color: var(--ink-soft);
  }
</style>
</head>
<body>
  <main class="cover">
    <div class="cover__art-top" role="img" aria-label="Grey geometric triangle pattern"></div>

    <div class="brand">
      <div class="brand__square"></div>
      <span class="brand__name">Tarnvale Cores</span>
    </div>

    <h1 class="report-title">Report Title here</h1>
    <p class="report-subtitle">Subtitle here</p>

    <section class="cover__band">
      <svg class="cover__band-notch" viewBox="0 0 50 25" aria-hidden="true">
        <polygon points="0,25 25,0 50,25" fill="var(--brand-yellow)"/>
      </svg>
      <div class="cover__art-bottom" role="img" aria-label="Deep yellow geometric triangle pattern"></div>

      <dl class="report-fields">
        <dt>Project</dt>
        <dd>Project name here</dd>
        <dt>Client</dt>
        <dd>Client name here</dd>
        <dt>Reference No.</dt>
        <dd>Reference here</dd>
      </dl>
    </section>
  </main>
</body>
</html>
```